Wordpress Theme Design for Family Law Firm

Hello, this is a WordPress theme design project, for a "Divorce and Family Law Mediation" practice.

I'd want the wordpress theme to be modeled loosely on this existing design from another one of our own sites: http://www.harbor-ledger-replies.example/

We want it to be bright and vibrant and convey a happy and relaxed feeling. The lines on it to not be sharp so more of the rounded edges and subtle shadows that you see on the example site.

Although built on WordPress, the site will be mostly static with fixed content pages, but including a blog feature.

The images will need to be different, but conveying a similar look and feel as the sample site. The colors from the sample site are close to what I'd like - but open to creative options.

It's important that the site looks professional, as well as friendly, and conveys the idea of mediation and relationships.

Important note: Traditional divorce website is for people looking to fight or being bullied.

Divorce mediation is for couples who have decided to split amicably so they're in a much more cooperative state of mind. There's not as much stress and anger. It's just about HOW we go about finalizing the process. There's light at the end of the tunnel.

With that in mind, the site should look friendly and happy, with an inspiring theme of a bright future.

Target Market(s)

The target market are people looking for amicable resolution, with a happy and uplifting attitude..

Traditional divorce websites are for people generally looking to fight or being bullied.

Divorce mediation (this website) is for couples who have decided to split amicably so they're in a much more cooperative state of mind. There's not as much stress and anger. It's just about HOW we go about finalizing the process. There's light at the end of the tunnel.

Industry/Entity Type

Family Law

Requirements
Must have
• Must have option for 1 or two sidebars for pages. This is because some of the internal pages will only have a single sidebar.

The footer will have the option for widgets.

```html
<!DOCTYPE html>
<html lang="en">
<head>
<meta charset="utf-8">
<title>Harbor Divorce &amp; Family Mediation</title>
<link href="https://fonts.googleapis.com/css2?family=Ubuntu:wght@400;500;700&family=Arimo:wght@400;700&display=swap" rel="stylesheet">
<style>
:root{
  --blue:#0d5ba8;
  --blue-dark:#0a4585;
  --orange:#f7941d;
  --text:#4a4a4a;
  --muted:#777;
  --line:#d9d9d9;
  --page-bg:#e9ebee;
  --cream:#faf8ef;
  --footer-bg:#e6e8ec;
}
*{box-sizing:border-box;margin:0;padding:0}
html,body{width:821px;height:1200px;overflow:hidden}
body{background:var(--page-bg);font-family:Arimo,Arial,sans-serif;color:var(--text);position:relative}
.page{position:absolute;left:82px;top:0;width:657px;height:1200px;background:#fff;box-shadow:0 0 6px rgba(0,0,0,.25)}
.abs{position:absolute}
h2,h3,.brand{font-family:Ubuntu,Arial,sans-serif}
.brand{left:8px;top:27px;font-size:16px;font-weight:700;color:var(--blue);line-height:1.05;width:210px;letter-spacing:.2px}
.phone{right:7px;top:9px;font:700 16px Ubuntu,Arial,sans-serif;color:#222;display:flex;align-items:center;gap:6px}
.phone .ico{width:17px;height:17px;background:var(--blue);border-radius:4px;display:flex;align-items:center;justify-content:center}
.nav{right:10px;top:41px;display:flex;gap:0;font-size:9.5px}
.nav a{color:#333;text-decoration:none;padding:4px 6.5px;text-transform:uppercase}
.nav a.active{background:var(--blue);color:#fff;font-weight:700;border-radius:2px}
.topline{left:0;top:70px;width:657px;height:2px;background:#4f8ccc}
.slider{left:18px;top:77px;width:621px;height:225px;background:linear-gradient(90deg,#eef2f6 0%,#e4e9ef 40%,#6b86a3 60%,#c9d3de 80%,#3b4f68 100%)}
.slide-copy{left:42px;top:151px;width:140px}
.slide-copy h2{font-size:20px;line-height:22px;color:var(--blue);font-weight:700;margin-bottom:3px;white-space:nowrap}
.slide-copy p{font-size:9px;line-height:12.5px;color:#444;text-align:justify}
.btn-orange{left:42px;top:219px;width:131px;height:25px;border-radius:3px;background:linear-gradient(#ffab2e,#f38a0c);color:#fff;font-size:9.5px;font-weight:700;display:flex;align-items:center;justify-content:center}
.arrow{top:164px;width:14px;height:34px;background:#333;color:#fff;font-size:13px;display:flex;align-items:center;justify-content:center}
.arrow.l{left:18px;border-radius:0 17px 17px 0}
.arrow.r{left:625px;border-radius:17px 0 0 17px}
.pager{left:309px;top:280px;width:64px;height:22px;background:var(--orange);border-radius:3px 3px 0 0;display:flex;align-items:center;justify-content:center;gap:4px}
.pager i{width:7px;height:7px;border-radius:50%;background:#fff}
.pager i.on{background:var(--blue)}
.feature{top:326px;width:150px}
.feature h3{font-size:12.5px;color:var(--blue);font-weight:700;margin-bottom:10px}
.feature .thumb{width:86px;height:44px;border:1px solid var(--line);padding:3px;background:#fff;box-shadow:0 1px 2px rgba(0,0,0,.1);margin-bottom:13px}
.feature .thumb div{width:100%;height:100%;background:linear-gradient(135deg,#7a5a44,#c9b39a 60%,#3d4756)}
.feature p{font-size:8.2px;line-height:12.3px;color:#555}
.feature a{display:block;margin-top:4px;font-size:8px;color:#666;text-decoration:underline}
.dash{height:0;border-top:1px dashed #c9c9c9}
.sidebar{left:483px;top:513px;width:168px;height:461px;background:var(--cream);border-left:1px solid #eee}
.sidebar h3{font-size:13.5px;color:var(--blue);margin:11px 0 7px 9px}
.sidebar ul{list-style:none;margin:0 8px}
.sidebar li{border-top:1px solid #e3e0d4;height:24.6px;display:flex;align-items:center;justify-content:space-between;font-size:8.2px;color:var(--blue);padding:0 2px 0 1px}
.sidebar li::after{content:"›";color:#999;font-size:10px}
.expert{left:8px;top:542px;width:253px}
.expert h2{font-size:14px;color:var(--blue);line-height:16px;margin-bottom:8px}
.expert p{font-size:8.3px;line-height:16.4px;color:#555;text-align:justify}
.expert p a{color:var(--blue);font-weight:700;text-decoration:underline;margin-left:10px}
.expert-photo{left:279px;top:543px;width:184px;height:130px;background:linear-gradient(120deg,#c4c9d2,#5d6e86 50%,#2a3447)}
.testi-h{left:8px;top:734px;font-size:13.5px;color:var(--blue)}
.testi{left:8px;top:763px;width:212px;height:125px;border:1px solid #eaeaea;border-radius:3px;padding:8px 10px;font-size:8.1px;line-height:16.4px;color:#555}
.testi em{display:block;font-family:Georgia,serif;font-weight:700;font-size:8px;line-height:14px;color:#444;margin-top:1px}
.tdots{left:192px;top:896px;display:flex;gap:3px}
.tdots i{width:7px;height:7px;border-radius:50%;background:#ccc}
.tdots i.on{background:var(--blue)}
.follow-h{left:9px;top:914px;font-size:13.5px;color:var(--blue)}
.social{left:9px;top:938px;display:flex;gap:7px}
.social i{width:19px;height:19px;border-radius:2px;display:block}
.contact{left:279px;top:726px;width:186px;height:230px;background:#f3f3f3;border:1px solid #ddd;border-radius:5px;padding:8px 15px}
.contact h2{font-size:14px;color:var(--blue);margin:0 0 9px 0}
.field{height:22px;background:#fff;border:1px solid #e2e2e2;border-radius:2px;font-size:8px;color:#888;padding:6px 8px;margin-bottom:5px}
.field.area{height:70px}
.btn-blue{margin-top:8px;height:22px;border-radius:3px;background:linear-gradient(#1a6cc0,#0a4585);color:#fff;font-size:8.3px;font-weight:700;display:flex;align-items:center;justify-content:center}
.footer{left:0;top:974px;width:657px;height:226px;background:var(--footer-bg);border-top:3px solid #1c5fa6}
.footer h4{font:700 9px Arimo,Arial,sans-serif;color:#444}
.fcol{top:34px}
.tweet{left:8px;top:56px;width:147px;height:92px;background:#fff;border-radius:3px;padding:12px 12px;font-size:8px;line-height:12.5px;color:#444;text-align:justify}
.tnav{left:118px;top:31px;display:flex;gap:2px}
.tnav i{width:12px;height:12px;border-radius:50%;background:#fff;border:1px solid #bbb;font-size:8px;display:flex;align-items:center;justify-content:center;font-style:normal;color:#444}
.office li{list-style:none;display:flex;gap:6px;font-size:8px;line-height:12.5px;color:#555;margin-bottom:7px}
.office .ic{width:9px;height:9px;border-radius:2px;background:#555;flex:none;margin-top:2px}
.post{font-size:8px;line-height:12.5px;color:#555;width:148px;margin-bottom:13px}
.post .meta{display:flex;justify-content:space-between;color:var(--blue);font-size:7.8px;margin-top:3px}
.git .in{height:15px;background:#fff;border:1px solid #d6d6d6;border-radius:2px;margin-bottom:4px;position:relative}
.git .in span{position:absolute;right:0;top:0;height:13px;padding:0 8px;background:#eef0f3;border-left:1px solid #d6d6d6;font-size:7.5px;line-height:13px;color:var(--blue)}
.git .ta{height:80px;background:#fff;border:1px solid #d6d6d6;border-radius:2px}
.git .send{margin-top:12px;width:74px;height:15px;background:#eef0f3;border:1px solid #c9c9c9;border-radius:2px;font-size:7.5px;color:var(--blue);text-align:center;line-height:13px}
.copy{left:14px;top:200px;font-size:8px;color:var(--blue)}
</style>
</head>
<body>
<div class="page">
  <header>
    <div class="abs brand">Harbor Divorce &amp; Family Mediation</div>
    <div class="abs phone"><span class="ico"><svg width="10" height="10" viewBox="0 0 24 24"><path fill="#fff" d="M6.6 10.8a15 15 0 0 0 6.6 6.6l2.2-2.2c.3-.3.7-.4 1-.2 1.1.4 2.3.6 3.6.6.6 0 1 .4 1 1V20c0 .6-.4 1-1 1A17 17 0 0 1 3 4c0-.6.4-1 1-1h3.5c.6 0 1 .4 1 1 0 1.3.2 2.5.6 3.6.1.3 0 .7-.2 1z"/></svg></span>123-456-789</div>
    <nav class="abs nav">
      <a class="active">Home</a><a>About Us</a><a>Divorce</a><a>Family Law</a><a>Testimonials</a><a>Blog</a><a>Contact Us</a>
    </nav>
    <div class="abs topline"></div>
  </header>

  <section>
    <div class="abs slider" role="img" aria-label="Photo of a smiling couple shaking hands with a mediator"></div>
    <div class="abs slide-copy">
      <h2>Split Amicably</h2>
      <p>There's not as much stress and anger. Light at the end of the Tunnel</p>
    </div>
    <div class="abs btn-orange">Contact Us</div>
    <div class="abs arrow l">‹</div>
    <div class="abs arrow r">›</div>
    <div class="abs pager"><i class="on"></i><i></i><i></i><i></i></div>
  </section>

  <section>
    <div class="abs feature" style="left:10px"><h3>Professional Approach</h3><div class="thumb"><div role="img" aria-label="Photo of professionals in a courtroom"></div></div><p>Lorem ipsum dolor sit amet, consectetuer adipiscing elit. Praesent aliquam, justo convallis luctus rutrum, erat nulla fermentum diam dolor site amet</p><a>Read More</a></div>
    <div class="abs feature" style="left:175px"><h3>Family Advisor</h3><div class="thumb"><div role="img" aria-label="Photo of a family meeting an advisor" style="background:linear-gradient(135deg,#e9ecef,#8d959e 60%,#2b2f36)"></div></div><p>Lorem ipsum dolor sit amet, consectetuer adipiscing elit. Praesent aliquam, justo convallis luctus rutrum, erat nulla fermentum diam dolor site amet</p><a>Read More</a></div>
    <div class="abs feature" style="left:342px"><h3>Amicable Divorce</h3><div class="thumb"><div role="img" aria-label="Photo of a couple in a library office" style="background:linear-gradient(135deg,#c98a55,#a44b34 55%,#4a2e24)"></div></div><p>Lorem ipsum dolor sit amet, consectetuer adipiscing elit. Praesent aliquam, justo convallis luctus rutrum, erat nulla fermentum diam dolor site amet</p><a>Read More</a></div>
    <div class="abs feature" style="left:508px"><h3>Qualified Solutions</h3><div class="thumb"><div role="img" aria-label="Photo of a team of legal professionals" style="background:linear-gradient(135deg,#d9dde2,#565a60 55%,#1f2226)"></div></div><p>Lorem ipsum dolor sit amet, consectetuer adipiscing elit. Praesent aliquam, justo convallis luctus rutrum, erat nulla fermentum diam dolor site amet</p><a>Read More</a></div>
  </section>

  <div class="abs dash" style="left:3px;top:513px;width:648px"></div>

  <aside class="abs sidebar">
    <h3>Family Law</h3>
    <ul>
      <li>Adoption</li><li>Child Abuse</li><li>Child Custody</li><li>Child Support</li><li>Divorce</li><li>Domestic Partnerships</li><li>Domestic Violence</li><li>Emancipation of Minors</li><li>Family Legal Help</li><li>Foster Care</li><li>Guardianship</li><li>Living Together</li><li>Marriage Law</li><li>Parental Rights and Liability</li><li>Paternity</li><li>Reproductive Rights</li><li>Surrogacy and Artificial Conception</li>
    </ul>
  </aside>

  <section>
    <div class="abs expert">
      <h2>We offer our clients an expert legal advice</h2>
      <p>Lorem ipsum dolor sit amet, consectetur adipisicing elit, sed do eiusmod tempor incididunt ut labore et dolore magna aliqua. Ut enim ad minim veniam, quis nostrud exercitation ullamco laboris nisi ut aliquip ex ea commodo consequat. Duis aute irure dolor in reprehenderit in voluptate velit esse cillum dolore eu fugiat nulla pariatur.<a>Read More</a></p>
    </div>
    <div class="abs expert-photo" role="img" aria-label="Photo of a businessman in a suit offering a handshake"></div>
  </section>

  <div class="abs dash" style="left:3px;top:697px;width:475px"></div>

  <section>
    <h2 class="abs testi-h">Client Testimonials</h2>
    <div class="abs testi">Sed ut perspiciatis unde omnis iste natus error sit voluptatem accusantium doloremque laudantium, totam rem aperiam, eaque ipsa quae ab illo inven-tore veritatis et quasi architecto beatae vitae dicta sunt explicabo. Nemo enim ipsam voluptatem quia voluptas sit aspernatur aut odit aut fugit.<em>Mrs. Lorem Ipsum</em></div>
    <div class="abs tdots"><i class="on"></i><i></i><i></i></div>
    <h2 class="abs follow-h">Follow Us</h2>
    <div class="abs social">
      <i style="background:#f08a24"></i><i style="background:#3bb0dd"></i><i style="background:#3a5a98"></i><i style="background:#cfd3da"></i><i style="background:#2a7bb5"></i>
    </div>
  </section>

  <section class="abs contact">
    <h2>Contact Us Today</h2>
    <div class="field">Name</div>
    <div class="field">E-mail</div>
    <div class="field">Phone</div>
    <div class="field area">Tell us about your case</div>
    <div class="btn-blue">Submit Information</div>
  </section>

  <footer class="abs footer">
    <h4 class="abs fcol" style="left:8px">Recent Tweets</h4>
    <div class="abs tnav"><i>‹</i><i>›</i></div>
    <div class="abs tweet">Lorem ipsum dolor sit amet, consectetur adipisicing elit, sed do eiusmod tempor incididunt ut labore et dolore magna aliqua. Ut enim ad minim veniam.</div>

    <h4 class="abs fcol" style="left:176px">Our Office</h4>
    <ul class="abs office" style="left:176px;top:56px;width:140px">
      <li><span class="ic"></span>123 Lorem Ipsum, Dole Sit City 456789 Consitectur</li>
      <li><span class="ic"></span>0123 456 789</li>
      <li><span class="ic"></span>0800 123 456</li>
      <li><span class="ic"></span>info@harborfamilymediation.example</li>
    </ul>

    <h4 class="abs fcol" style="left:341px">Recent Blog Post</h4>
    <div class="abs" style="left:341px;top:55px">
      <div class="post">Lorem ipsum dolor sit amet, consec-tetur adipisicing<div class="meta"><span>Nov. 26, 2012</span><span>3 comments</span></div></div>
      <div class="post">Lorem ipsum dolor sit amet, consec-tetur adipisicing<div class="meta"><span>Nov. 25, 2012</span><span>5 comments</span></div></div>
      <div class="post">Lorem ipsum dolor sit amet, consec-tetur adipisicing<div class="meta"><span>Nov. 23, 2012</span><span>7 comments</span></div></div>
    </div>

    <h4 class="abs fcol" style="left:508px">Get in Touch</h4>
    <div class="abs git" style="left:508px;top:56px;width:144px">
      <div class="in"><span>Name</span></div>
      <div class="in"><span>E-mail</span></div>
      <div class="ta"></div>
      <div class="send">Send Message</div>
    </div>

    <div class="abs copy">Copyright 2012, Harbor Divorce and Family Mediation. All Rights Reserved.</div>
  </footer>
</div>
</body>
</html>
```